Game, Voice & Dedicated Server Company Needs a Business Card Design

We need a new business card design, centered around our new logo (PSD provided below).

Designs that we do like:
https://pixelmarsh.net/item/corporate-business-card/5382017?s_rank=43 (needs to be made more eye catching)

Our main areas of business are:
- Dedicated Servers
- Game Servers
- Voice Servers
- Mitigation Security Specialists

Industry/Entity Type

Business

Contact Information for Business Card

On the card: (and anything else you would suggest)
- Staff member name
- Staff member position in company
- Staff member phone number
- Staff member email
- Other / Staff member Skype
- Website link

Colors
9bcb3c
abd036

Requirements
Must have
• Design of Card:
• - Green (same green as the logo)
• - Business / Corporate design
• - Something a little different / abstract that shouts premium

```html
<!DOCTYPE html>
<html lang="en">
<head>
<meta charset="utf-8">
<title>Brightpath Hosting – Business Card</title>
<link rel="stylesheet" href="https://fonts.googleapis.com/css2?family=Roboto:wght@400;500;700&display=swap">
<style>
  :root {
    --green: #9bcb3c;
    --green-bright: #abd036;
    --green-neon: #b6ec2a;
    --grey-text: #8a8a8a;
    --grey-dark: #6e6e6e;
    --card-white: #ffffff;
    --card-grey: #eeeeee;
    --backdrop: #e4e4e2;
  }
  * { box-sizing: border-box; margin: 0; padding: 0; }
  html, body {
    width: 1200px; height: 1023px; overflow: hidden;
    background: var(--backdrop);
    font-family: "Roboto", Arial, sans-serif;
  }
  .canvas { position: relative; width: 1200px; height: 1023px; }

  .card {
    position: absolute;
    width: 620px; height: 354px;
    border-radius: 18px;
    overflow: hidden;
    box-shadow: 0 6px 20px rgba(0,0,0,.14);
  }

  /* Front */
  .card--front { left: 70px; top: 80px; background: var(--card-white); }
  .swoosh {
    position: absolute; right: -140px; top: -260px;
    width: 700px; height: 620px; border-radius: 50%;
    background: radial-gradient(circle at 30% 70%, #ffffff 0 42%, var(--green-neon) 52%, #d6f5a8 64%, #e9f7e4 78%, #f4faf3 100%);
  }
  .front-brand {
    position: absolute; left: 44px; top: 112px;
    display: flex; align-items: center; gap: 14px;
  }
  .brand-mark { width: 34px; height: 34px; background: var(--green); flex: none; }
  .brand-name {
    font-weight: 700; color: var(--green);
    font-size: 30px; line-height: 1; letter-spacing: .5px;
  }
  .contact { position: absolute; left: 44px; top: 196px; }
  .contact-row {
    display: flex; align-items: center; gap: 10px;
    font-size: 12px; line-height: 16px; color: var(--grey-text); margin-top: 3px;
  }
  .contact-row svg { width: 15px; height: 15px; flex: none; }
  .contact-row.person { margin-top: 0; }
  .person-name { font-size: 16px; line-height: 20px; font-weight: 500; color: var(--grey-dark); }
  .person-title { font-size: 11px; line-height: 14px; color: var(--green); margin: 0 0 2px 26px; }

  /* Back */
  .card--back {
    left: 510px; top: 590px;
    background: linear-gradient(150deg, #fafafa 0%, var(--card-grey) 55%, #e2e2e2 100%);
  }
  .stripe { position: absolute; top: 0; bottom: 0; width: 16px; background: var(--green-bright); }
  .stripe--left { left: 18px; }
  .stripe--right { right: 18px; }
  .back-brand {
    position: absolute; inset: 0;
    display: flex; flex-direction: column; align-items: center; justify-content: center; gap: 20px;
  }
  .back-brand .brand-mark { width: 56px; height: 56px; }
  .back-brand .brand-name { font-size: 46px; text-align: center; }
</style>
</head>
<body>
<main class="canvas">

  <section class="card card--front" aria-label="Card front">
    <div class="swoosh" role="img" aria-label="Abstract green light swoosh"></div>
    <div class="front-brand">
      <span class="brand-mark"></span>
      <span class="brand-name">BRIGHTPATH<br>HOSTING</span>
    </div>
    <div class="contact">
      <div class="contact-row person">
        <svg viewBox="0 0 16 16"><circle cx="8" cy="8" r="8" fill="var(--green)"/><circle cx="8" cy="6.2" r="2.4" fill="#fff"/><path d="M3.8 12.5c.8-2.2 2.3-3.2 4.2-3.2s3.4 1 4.2 3.2z" fill="#fff"/></svg>
        <span class="person-name">Your Name</span>
      </div>
      <div class="person-title">Title</div>
      <div class="contact-row">
        <svg viewBox="0 0 16 16"><rect x="4" y="1" width="8" height="14" rx="1.5" fill="none" stroke="var(--green)" stroke-width="1.4"/><circle cx="8" cy="12.5" r=".9" fill="var(--green)"/></svg>
        <span>00-555-01987</span>
      </div>
      <div class="contact-row">
        <svg viewBox="0 0 16 16"><circle cx="8" cy="8" r="7" fill="var(--green)"/></svg>
        <span>Your id</span>
      </div>
      <div class="contact-row">
        <svg viewBox="0 0 16 16" fill="none" stroke="var(--green)" stroke-width="1.2"><circle cx="8" cy="8" r="6.5"/><ellipse cx="8" cy="8" rx="3" ry="6.5"/><path d="M1.5 8h13M2.5 4.8h11M2.5 11.2h11"/></svg>
        <span>www.your web.com</span>
      </div>
      <div class="contact-row">
        <svg viewBox="0 0 16 16"><path d="M8 15s5-5.2 5-8.6A5 5 0 0 0 3 6.4C3 9.8 8 15 8 15z" fill="var(--green)"/><circle cx="8" cy="6.4" r="1.8" fill="#fff"/></svg>
        <span>Your adress in a line</span>
      </div>
    </div>
  </section>

  <section class="card card--back" aria-label="Card back">
    <span class="stripe stripe--left"></span>
    <span class="stripe stripe--right"></span>
    <div class="back-brand">
      <span class="brand-mark"></span>
      <span class="brand-name">BRIGHTPATH<br>HOSTING</span>
    </div>
  </section>

</main>
</body>
</html>
```